Box Packaging Design for Yoga Foam Roller

We need a box packaging design for our yoga foam roller.

1. dimensions of box: 31x16x16cm. see template.jpg for design layout & measurements. box example shows an example product & box dimensions.

2. the design style should have an organic, earth-friendly touch to it with natural colors. reference design.jpg shows the exact design style

3. please generally use wavy lines for the edges instead of sharp straight lines.

4. its a 2 color print design: light brown (see reference design) and charcoal dark blue. the "3rd color" is the brown carton base color.

5. schematic drawing.jpg shows a general blueprint for the packaging design and the placement of the elements.

6. please include yoga person from yoga silhouette.jpg and logo from logo.jpg like shown in the schematic drawing

7. please include barcode label.pdf as shown in the schematic drawing

Target Market(s)

We are a young company from Germany selling yoga and sports products in Europe. Our main markets are Germany, UK, France, Italy and Spain. For our latest product, a Yoga Foam Roller.

The target audience are people which are into Yoga, Health, Pilates, Sports and Fitness. The roller can be used to massage tissues and muscles or for a pre-workout warmup program.

Requirements
Must have
• - design style like reference design.jpg
• - dimensions according to template.jpg
• - barcode label
• - "Desigend in Germany"
• - "Made in China"
• - "Quiet Harbor" & logo according to project description, "Faszienrolle", "schwarz/blau"
• - two color design (carton background = "3rd color")
Nice to have
• - see project description (wavy lines, yoga person silhouette, ...)
• - "100% Satisfaction Guarantee" label
• - "Money Back Guarantee" label

```html
<!DOCTYPE html>
<html lang="de">
<head>
<meta charset="utf-8">
<title>Quiet Harbor – Faszienrolle Box Dieline</title>
<link rel="stylesheet" href="https://fonts.googleapis.com/css2?family=Lato:ital,wght@0,300;0,400;1,400&family=Roboto:wght@400;500&display=swap">
<style>
  :root{
    --kraft:#8a7556;
    --kraft-deep:#7d6a4d;
    --cream:#ece4d5;
    --ink:#8c7657;
    --cut:#e0231f;
    --fold:#4a3f33;
    --page:#ffffff;
  }
  html,body{margin:0;padding:0;overflow:hidden;background:var(--page);}
  .canvas{width:1200px;height:1190px;display:block;}
  .piece{fill:var(--kraft);stroke:var(--cut);stroke-width:2;stroke-linejoin:round;}
  .fold{stroke:var(--fold);stroke-width:1;fill:none;}
  .cream{fill:var(--cream);}
  .kraft{fill:var(--kraft);}
  .label-de{fill:var(--cream);}
  .label-en{fill:var(--kraft-deep);}
  .brand{font-family:'Lato',sans-serif;font-weight:400;letter-spacing:5px;font-size:14px;fill:var(--ink);}
  .brand-flap{font-family:'Lato',sans-serif;font-weight:400;letter-spacing:5px;font-size:18px;fill:var(--cream);}
  .product{font-family:'Lato',sans-serif;font-weight:300;font-size:50px;fill:var(--ink);}
  .variant{font-family:'Lato',sans-serif;font-weight:400;font-size:14px;letter-spacing:2px;fill:var(--ink);}
  .tagline{font-family:'Lato',sans-serif;font-style:italic;font-size:19px;fill:var(--cream);}
  .origin{font-family:'Roboto',sans-serif;font-weight:500;font-size:12.5px;fill:var(--ink);}
  .bullets{font-family:'Roboto',sans-serif;font-size:9.6px;}
  .bullets-de{fill:var(--ink);}
  .bullets-en{fill:var(--cream);}
  .lang{font-family:'Roboto',sans-serif;font-weight:500;font-size:11px;}
  .silhouette{fill:var(--kraft);}
</style>
</head>
<body>
<svg class="canvas" viewBox="0 0 1500 1500" preserveAspectRatio="none" xmlns="http://www.w3.org/2000/svg">

  <!-- die pieces -->
  <g class="dieline">
    <path class="piece" d="M95,108 L105,68 Q108,57 120,57 L400,57 Q412,57 416,68 L427,108 L427,435 L95,435 Z"/>
    <rect class="piece" x="95" y="435" width="332" height="635"/>
    <path class="piece" d="M425,435 L437,397 Q441,385 452,385 L722,385 Q734,385 738,397 L750,435 Z"/>
    <path class="piece" d="M425,1068 L437,1106 Q441,1118 452,1118 L722,1118 Q734,1118 738,1106 L750,1068 Z"/>
    <rect class="piece" x="425" y="435" width="325" height="633"/>
    <rect class="piece" x="750" y="435" width="328" height="633"/>
    <path class="piece" d="M750,1068 L1080,1068 L1080,1395 L1070,1432 Q1066,1446 1054,1446 L776,1446 Q764,1446 760,1432 L750,1395 Z"/>
    <path class="piece" d="M1078,435 L1090,397 Q1094,385 1105,385 L1378,385 Q1390,385 1394,397 L1405,435 Z"/>
    <path class="piece" d="M1078,1068 L1090,1106 Q1094,1118 1105,1118 L1378,1118 Q1390,1118 1394,1106 L1405,1068 Z"/>
    <rect class="piece" x="1078" y="435" width="327" height="633"/>
    <path class="piece" d="M1405,438 L1440,448 Q1458,453 1458,468 L1458,1040 Q1458,1054 1440,1058 L1405,1068 Z"/>
  </g>

  <!-- printed areas -->
  <path class="cream" d="M95,990 Q115,984 135,989 T175,988 T215,991 T255,987 T295,990 T335,986 T375,990 T415,988 T455,991 T495,986 T535,990 T575,987 T615,991 T655,987 T695,990 T750,988 L750,1068 L95,1068 Z"/>
  <path class="cream" d="M762,447 L1395,447 L1395,983 Q1375,978 1355,984 T1315,982 T1275,986 T1235,981 T1195,985 T1155,982 T1115,986 T1075,981 T1035,985 T995,982 T955,986 T915,981 T875,985 T835,982 T795,986 T762,983 Z"/>

  <rect class="silhouette" x="806" y="765" width="218" height="222" rx="90" role="img" aria-label="Silhouette of a person sitting cross-legged in a meditation pose"/>

  <!-- fold lines -->
  <g class="fold">
    <line x1="95" y1="108" x2="427" y2="108"/>
    <line x1="95" y1="435" x2="1405" y2="435"/>
    <line x1="95" y1="1068" x2="1405" y2="1068"/>
    <line x1="425" y1="435" x2="425" y2="1068"/>
    <line x1="750" y1="435" x2="750" y2="1068"/>
    <line x1="1078" y1="435" x2="1078" y2="1068"/>
    <line x1="1405" y1="435" x2="1405" y2="1068"/>
    <line x1="750" y1="1395" x2="1080" y2="1395"/>
  </g>

  <!-- top tuck flap -->
  <text class="brand-flap" x="261" y="280" text-anchor="middle">QUIET HARBOR</text>

  <!-- front panel -->
  <text class="brand" x="915" y="631" text-anchor="middle">QUIET HARBOR</text>
  <text class="product" x="913" y="714" text-anchor="middle">Faszienrolle</text>
  <text class="variant" x="913" y="737" text-anchor="middle">schwarz/blau</text>
  <text class="tagline" x="915" y="1046" text-anchor="middle">Yoga Foam Roller with 100% Love</text>

  <!-- side panel: origin -->
  <text class="origin" x="120" y="1026">Designed in Germany</text>
  <text class="origin" x="120" y="1042">Made In China</text>

  <!-- German benefits -->
  <rect class="label-de" x="480" y="790" width="215" height="148" rx="8"/>
  <text class="lang" x="493" y="810" fill="#8c7657">DE</text>
  <g class="bullets bullets-de">
    <text x="494" y="823">▪ <tspan>Für hocheffektives Faszientraining</tspan></text>
    <text x="494" y="837">▪ Steigert Leistungsvermögen</text>
    <text x="502" y="848">und elastizität der Muskulatur</text>
    <text x="494" y="862">▪ Löst Verspannungen und Verklebungen</text>
    <text x="502" y="873">der Faszien</text>
    <text x="494" y="887">▪ Steigert Durchblutung und</text>
    <text x="502" y="898">Regenerationsvermögen</text>
    <text x="494" y="912">▪ 100% frei von Chemikalien</text>
    <text x="494" y="927">▪ Sehr gut Hautverträglich</text>
  </g>

  <!-- English benefits -->
  <rect class="label-en" x="1134" y="799" width="215" height="139" rx="8"/>
  <text class="lang" x="1147" y="819" fill="#ece4d5">EN</text>
  <g class="bullets bullets-en">
    <text x="1148" y="832">▪ For a highly effective workout</text>
    <text x="1148" y="847">▪ Increases performance and muscle</text>
    <text x="1156" y="858">elasticity</text>
    <text x="1148" y="872">▪ Alleviates strains and posture problems</text>
    <text x="1148" y="887">▪ Increases blood circulation, rejuvinates</text>
    <text x="1156" y="898">muscles</text>
    <text x="1148" y="912">▪ 100% free of chemicals</text>
    <text x="1148" y="926">▪ Skin-friendly</text>
  </g>
</svg>
</body>
</html>
```